HCW Business Card Design

I am a wedding and event Planner. I have just completed a name change from Gatherings by Odette to The Hollow Crest Workshop and I just received my new logo and need new business cards to match my new brand. Elegant, chic and upscale yet simple. I am drafting a new website on my old (for drafting purposes). You can take a look and it will give you an idea of the direction of my brand. (www.gatheringsbyodette.example). I would like gray and white colors and it can be a shaded mixture of grays. I am open in regard to placement of the information

Target Market(s)

Brides, Corporate Companies, Families etc.

Industry/Entity Type

Wedding

Contact Information for Business Card

The Hollow Crest Workshop
www.myhollowcrestworkshop.example
Event Planning and Design Firm
Odette M. Vance, Owner/CEO
Certified Event & Wedding Planner
T: (555) 240-7318 | F: (555) 617-4052
E: wegather@myhollowcrestworkshop.example
(please put T, E & F letters in a script font)

Love to Plan. Plan to Live. Live to Love. (rb)

(social icons instead of text)
twitter: @hollowcrestwork1
facebook: @thehollowcrestwork
Pinterest: @hollowcrestwork
instagram: @thehollowcrestwork1

Can we put a barcode leading to my website

```html
<!DOCTYPE html>
<html lang="en">
<head>
<meta charset="UTF-8">
<title>The Hollow Crest Workshop – Business Card</title>
<link href="https://fonts.googleapis.com/css2?family=Pinyon+Script&family=Raleway:wght@200&family=Ubuntu:wght@400&display=swap" rel="stylesheet">
<style>
  :root {
    --paper: #ffffff;
    --brand-grey: #8a9393;
    --mark-grey: #5d6b6b;
    --band-top: #6f8080;
    --band-mid: #5f7171;
    --band-low: #9aa6a6;
    --ink: #4f5555;
    --text-light: #ffffff;
    --rose-tone: #b9c2c0;
    --rose-deep: #8f9a98;
  }
  html, body {
    margin: 0;
    padding: 0;
    overflow: hidden;
    background: var(--paper);
  }
  .card {
    position: relative;
    width: 1200px;
    height: 702px;
    background: var(--paper);
    overflow: hidden;
  }
  .brand-mark {
    position: absolute;
    left: 177px;
    top: 25px;
    width: 204px;
    height: 204px;
  }
  .brand-name {
    position: absolute;
    left: 384px;
    top: 100px;
    margin: 0;
    font-family: "Raleway", sans-serif;
    font-weight: 200;
    font-size: 35px;
    letter-spacing: 2px;
    color: var(--brand-grey);
    white-space: nowrap;
  }
  .name-band {
    position: absolute;
    left: 0;
    top: 244px;
    width: 1200px;
    height: 157px;
    background: linear-gradient(to bottom,
      var(--band-top) 0%,
      var(--band-mid) 55%,
      var(--band-mid) 62%,
      var(--band-low) 100%);
  }
  .person-name {
    position: absolute;
    left: 0;
    width: 1350px;
    top: 8px;
    margin: 0;
    text-align: center;
    font-family: "Pinyon Script", cursive;
    font-weight: 400;
    font-size: 68px;
    line-height: 1.2;
    color: var(--text-light);
  }
  .person-title {
    position: absolute;
    left: 337px;
    top: 117px;
    margin: 0;
    font-family: "Ubuntu", sans-serif;
    font-size: 24px;
    letter-spacing: 1.4px;
    color: var(--text-light);
    white-space: nowrap;
  }
  .tagline {
    position: absolute;
    left: 391px;
    width: 600px;
    top: 428px;
    margin: 0;
    text-align: center;
    font-family: "Pinyon Script", cursive;
    font-size: 42px;
    line-height: 48px;
    color: var(--ink);
  }
  .roses {
    position: absolute;
    left: 735px;
    top: 426px;
    width: 465px;
    height: 276px;
    background: radial-gradient(ellipse at 85% 75%,
      var(--rose-deep) 0%,
      var(--rose-tone) 40%,
      rgba(255,255,255,0) 75%);
  }
</style>
</head>
<body>
  <main class="card">
    <svg class="brand-mark" viewBox="0 0 204 204" aria-hidden="true">
      <circle cx="102" cy="102" r="96" fill="none" stroke="var(--mark-grey)" stroke-width="3"/>
    </svg>
    <h1 class="brand-name">THE HOLLOW CREST WORKSHOP</h1>

    <section class="name-band">
      <h2 class="person-name">Odette M. Vance</h2>
      <p class="person-title">Owner/CEO Certified Event &amp; Wedding Planner</p>
    </section>

    <p class="tagline">Love to Plan. Plan to Live.<br>Live to Love.</p>

    <div class="roses" role="img" aria-label="Soft grey photograph of a bouquet of roses"></div>
  </main>
</body>
</html>
```